A label for my commercially sold local honey. This is a LABEL not a logo

3 inches high
2 inches wide

Target Market(s)

Customers who like "local" honey

Logo Text

Wildflower Honey -- 100% Pure & Unfiltered -- Florida

Logo styles of interest
Wordmark Logo
Requirements
Must have
• Wildflower Honey -- 100% Pure & Unfiltered -- Florida

Florida should be dominant

3 inches high / 2 inches wide

```html
<!DOCTYPE html>
<html lang="en">
<head>
<meta charset="utf-8">
<title>Wildflower Honey Label</title>
<link href="https://fonts.googleapis.com/css2?family=Sansita:wght@800&family=Montserrat:wght@500;700&family=Questrial&display=swap" rel="stylesheet">
<style>
  :root {
    --backdrop: #2a1d15;
    --kraft: #e2c8ab;
    --kraft-light: #e8d2b8;
    --kraft-deep: #cfb08e;
    --field-green: #4f6653;
    --stripe-green: #44594a;
    --cream: #fbf6ee;
    --honey-tan: #dbb68d;
    --slate: #48524d;
    --brown-ink: #5a4636;
  }
  * { margin: 0; padding: 0; box-sizing: border-box; }
  html, body {
    width: 1200px; height: 1181px; overflow: hidden;
    background: var(--backdrop);
  }
  .canvas { position: relative; width: 1200px; height: 1181px; }
  .label {
    position: absolute; left: 270px; top: 95px;
    width: 660px; height: 990px;
    background: var(--kraft);
    overflow: hidden;
  }
  .label-shapes { position: absolute; inset: 0; }
  .brand-seal {
    position: absolute; left: 238px; top: 40px;
    width: 184px; height: 184px; border-radius: 50%;
    background: var(--kraft-light);
    border: 3px solid var(--kraft-deep);
    display: flex; align-items: center; justify-content: center;
    font-family: "Montserrat", sans-serif; font-weight: 700;
    font-size: 26px; color: var(--brown-ink); letter-spacing: 0.5px;
  }
  .product-name {
    position: absolute; left: 0; width: 100%; top: 355px;
    text-align: center;
    font-family: "Sansita", sans-serif; font-weight: 800;
    font-size: 96px; line-height: 1; color: var(--cream);
  }
  .product-type {
    position: absolute; left: 0; width: 100%; top: 452px;
    text-align: center;
    font-family: "Montserrat", sans-serif; font-weight: 700;
    font-size: 58px; line-height: 1; letter-spacing: 1px;
    color: var(--honey-tan);
  }
  .purity-box {
    position: absolute; left: 180px; top: 580px;
    width: 300px; height: 160px;
    background: var(--kraft-deep);
    display: flex; flex-direction: column; align-items: center; justify-content: center;
    color: var(--brown-ink);
  }
  .purity-percent {
    font-family: "Questrial", sans-serif; font-size: 56px; line-height: 1;
  }
  .purity-note {
    font-family: "Questrial", sans-serif; font-size: 22px; line-height: 1.05;
    text-align: center; letter-spacing: 0.5px;
  }
  .origin {
    position: absolute; left: 0; width: 100%; top: 855px;
    text-align: center;
    font-family: "Questrial", sans-serif;
    font-size: 104px; line-height: 1; letter-spacing: 2px;
    color: var(--slate);
  }
</style>
</head>
<body>
<div class="canvas">
  <div class="label">
    <svg class="label-shapes" width="660" height="990" viewBox="0 0 660 990">
      <defs>
        <pattern id="pinstripe" width="8" height="10" patternUnits="userSpaceOnUse">
          <rect width="8" height="10" fill="var(--field-green)"/>
          <rect width="2" height="10" fill="var(--stripe-green)"/>
        </pattern>
      </defs>
      <path d="M0 220 H660 V590 Q330 540 0 590 Z" fill="url(#pinstripe)"/>
      <rect role="img" aria-label="Row of honeycomb cells" x="0" y="190" width="660" height="40" fill="var(--kraft-deep)"/>
      <rect role="img" aria-label="Faint sunburst flower pattern" x="0" y="590" width="660" height="250" fill="var(--kraft-light)" opacity="0.45"/>
    </svg>
    <div class="brand-seal">Meadowline</div>
    <div class="product-name">Wildflower</div>
    <div class="product-type">HONEY</div>
    <div class="purity-box">
      <div class="purity-percent">100%</div>
      <div class="purity-note">PURE &amp;<br>UNFILTERED</div>
    </div>
    <div class="origin">FLORIDA</div>
  </div>
</div>
</body>
</html>
```